Birchford Realty Business Card

Business Card:

Somewhere on front of card, please include Broker License Number: 5839162

Website is BirchfordRealty.example

Address is:
7218 Crestover Ave E
Saginaw, MI 48271

I'll let you use creative freedom on the rest; we obviously need Name, Title, Email (@BirchfordRealty.example), Office Phone, Cell Phone.

Don't want any special die-cutting, just a standard size business card.

On the back, include a place for the date and time of an appointment to be written in pen.

Requirements
Must have
• Our logo, attached to email.

```html
<!DOCTYPE html>
<html lang="en">
<head>
<meta charset="utf-8">
<title>Birchford Realty Business Card</title>
<link href="https://fonts.googleapis.com/css2?family=Open+Sans:wght@400;600;700&display=swap" rel="stylesheet">
<style>
  :root {
    --navy: #2b2a7c;
    --navy-deep: #15145a;
    --navy-light: #4a4aa6;
    --cyan: #1fb0e6;
    --grey: #9a9aa6;
    --icon: #8a8a95;
    --ink: #2b2a7c;
    --paper: #ffffff;
    --backdrop: #e9e9ee;
  }
  * { box-sizing: border-box; margin: 0; padding: 0; }
  html, body { width: 1200px; height: 913px; overflow: hidden; }
  body {
    background: var(--backdrop);
    font-family: "Open Sans", Arial, sans-serif;
    position: relative;
  }
  .card {
    position: absolute;
    width: 540px;
    height: 309px;
    top: 302px;
    overflow: hidden;
    box-shadow: 0 6px 18px rgba(0,0,0,.18);
  }

  /* Front */
  .card-front { left: 40px; background: var(--paper); }
  .brand-front {
    position: absolute; right: 40px; top: 42px;
    display: flex; align-items: center; gap: 9px;
    color: var(--navy); font-weight: 700; font-size: 28px; line-height: 1; white-space: nowrap;
  }
  .brand-mark { width: 12px; height: 12px; background: currentColor; flex: none; }
  .front-rule {
    position: absolute; left: 230px; right: 40px; top: 86px; height: 2px;
    background: var(--cyan);
  }
  .identity { position: absolute; left: 40px; top: 96px; padding-left: 14px; }
  .identity::before {
    content: ""; position: absolute; left: 0; top: 4px; width: 5px; height: 34px;
    background: var(--grey);
  }
  .person-name { color: var(--ink); font-weight: 700; font-size: 17px; letter-spacing: .3px; line-height: 22px; }
  .person-title { color: var(--grey); font-size: 11px; letter-spacing: 1px; line-height: 16px; }
  .contact { position: absolute; left: 54px; top: 148px; color: var(--ink); font-size: 12.5px; line-height: 17px; }
  .address { margin-bottom: 8px; }
  .contact-list { list-style: none; }
  .contact-list li { display: flex; align-items: center; gap: 8px; white-space: nowrap; }
  .contact-list svg { width: 11px; height: 11px; flex: none; }
  .license {
    position: absolute; right: 40px; bottom: 46px;
    color: var(--grey); font-size: 11px; letter-spacing: .4px; white-space: nowrap;
  }
  .front-band {
    position: absolute; left: 0; right: 0; bottom: 0; height: 34px;
    background: var(--navy);
  }

  /* Back */
  .card-back {
    left: 620px;
    background: linear-gradient(160deg, var(--navy-light) 0%, var(--navy) 45%, var(--navy-deep) 100%);
  }
  .brand-back {
    position: absolute; left: 32px; top: 168px;
    display: flex; align-items: center; gap: 9px;
    color: var(--paper); font-weight: 700; font-size: 28px; line-height: 1; white-space: nowrap;
  }
  .appointment {
    position: absolute; right: 32px; top: 56px; width: 190px;
    color: var(--paper); font-size: 13px;
  }
  .appointment-title { font-weight: 600; font-size: 14px; margin-bottom: 22px; }
  .field { display: flex; align-items: flex-end; gap: 6px; margin-bottom: 24px; }
  .field-line { flex: 1; border-bottom: 1.5px dotted var(--paper); height: 1px; margin-bottom: 4px; }
  .back-band {
    position: absolute; left: 0; right: 0; bottom: 0; height: 34px;
    background: var(--paper);
  }
</style>
</head>
<body>
  <section class="card card-front" aria-label="Business card front">
    <div class="brand-front"><span class="brand-mark"></span>Birchford Realty</div>
    <div class="front-rule"></div>
    <div class="identity">
      <p class="person-name">DARA WHITLOCK</p>
      <p class="person-title">OWNER</p>
    </div>
    <div class="contact">
      <p class="address">7218 Crestover Ave E<br>Saginaw, MI 48271</p>
      <ul class="contact-list">
        <li><svg viewBox="0 0 12 12"><path d="M2 1h3l1 3-1.5 1a6 6 0 0 0 2.5 2.5L8 6l3 1v3c0 .6-.4 1-1 1A9 9 0 0 1 1 2c0-.6.4-1 1-1z" fill="#8a8a95"/></svg>+33 2460-5512</li>
        <li><svg viewBox="0 0 12 12"><rect x="3" y="1" width="6" height="10" rx="1" fill="none" stroke="#8a8a95" stroke-width="1.3"/></svg>+33 2460-5534</li>
        <li><svg viewBox="0 0 12 12"><rect x="1" y="2.5" width="10" height="7" fill="none" stroke="#8a8a95" stroke-width="1.2"/><path d="M1 2.5l5 4 5-4" fill="none" stroke="#8a8a95" stroke-width="1.2"/></svg>@BirchfordRealty.example</li>
        <li><svg viewBox="0 0 12 12"><circle cx="6" cy="6" r="5" fill="none" stroke="#8a8a95" stroke-width="1.2"/><path d="M1 6h10M6 1c-2 3-2 7 0 10M6 1c2 3 2 7 0 10" fill="none" stroke="#8a8a95" stroke-width="1"/></svg>www.BirchfordRealty.example</li>
      </ul>
    </div>
    <p class="license">Broker License #5839162</p>
    <div class="front-band"></div>
  </section>

  <section class="card card-back" aria-label="Business card back">
    <div class="appointment">
      <p class="appointment-title">Appointment:</p>
      <div class="field"><span>Date:</span><span class="field-line"></span></div>
      <div class="field"><span>Time:</span><span class="field-line"></span></div>
    </div>
    <div class="brand-back"><span class="brand-mark"></span>Birchford Realty</div>
    <div class="back-band"></div>
  </section>
</body>
</html>
```